Tide Harbor Finance Business Cards

Looking for a business card for a new mortgage broking business. Name of the business is Tide Harbor Finance. Purpose of the business is to build trust and strong relationships with clients to then assist them with your mortgage lending needs. Most relationships within the business start off as an enquiry, and then can evolve into a 10+ year relationship, servicing clients from purchasing a new home to then upgrading for their family and even then assisting their children with their first home purchase. Business card should communicate financial security and trust.

Target Market(s)

Targeting professional clients who are looking to build a relationship with a knowledgeable mortgage professional

Industry/Entity Type

Finance - Home Loans

Contact Information for Business Card

Peter Colburn, Director, mobile: 0427 903186, email:peter@tideharborfinance.com.au, website: www.tideharborfinance.com.au

Font styles to use
Sans Serif

Requirements
Must have
• On the front: Must have company logo, contact details as above. On the back: slogan, 'Clear Options, Calm Decisions', plus listing services offered: home loans, investment loans, first home buyers, refinancing, car finance

```html
<!DOCTYPE html>
<html lang="en">
<head>
<meta charset="utf-8">
<title>Tide Harbor Finance Business Cards</title>
<link href="https://fonts.googleapis.com/css2?family=Jost:wght@400;500;700&display=swap" rel="stylesheet">
<style>
  :root {
    --navy: #0b4a75;
    --orange: #f0a020;
    --gold-line: #e2c08a;
    --ink: #2f3a45;
    --card: #ffffff;
    --backdrop: #e6e8ea;
  }
  * { box-sizing: border-box; margin: 0; padding: 0; }
  html, body { width: 1200px; height: 900px; overflow: hidden; }
  body {
    background: var(--backdrop);
    font-family: "Jost", sans-serif;
    position: relative;
  }
  .card {
    position: absolute;
    width: 760px;
    height: 430px;
    background: var(--card);
    border-radius: 36px;
    overflow: hidden;
    box-shadow: 0 10px 30px rgba(0,0,0,.18);
  }
  .card--back { left: 60px; top: 20px; }
  .card--front { left: 380px; top: 450px; }
  .card__bands { position: absolute; inset: 0; }
  .brand {
    position: absolute;
    left: 60px;
    top: 130px;
    display: flex;
    align-items: center;
    gap: 18px;
  }
  .brand__mark {
    width: 90px; height: 90px;
    border-radius: 50%;
    border: 6px solid var(--navy);
    flex: none;
  }
  .brand__name {
    color: var(--navy);
    font-weight: 500;
    font-size: 34px;
    line-height: 1;
    text-transform: uppercase;
    letter-spacing: -0.5px;
  }
  .divider {
    position: absolute;
    left: 370px;
    top: 100px;
    width: 1.5px;
    height: 150px;
    background: var(--gold-line);
  }
  .details {
    position: absolute;
    left: 395px;
    top: 95px;
    color: var(--ink);
  }
  .details__title {
    color: var(--navy);
    font-weight: 700;
    font-size: 22px;
    margin-bottom: 6px;
  }
  .services { list-style: none; font-size: 19px; line-height: 1.45; }
  .services li { display: inline; margin-right: 8px; }
  .services .tick { color: var(--navy); margin-right: 4px; }
  .person__name {
    color: var(--navy);
    font-weight: 700;
    font-size: 24px;
    text-transform: uppercase;
    line-height: 1.1;
  }
  .person__role { font-size: 19px; margin-bottom: 10px; }
  .contact { list-style: none; font-size: 19px; line-height: 1.55; }
  .contact li { display: flex; align-items: center; gap: 10px; }
  .contact svg { width: 18px; height: 18px; flex: none; }
  .slogan {
    position: absolute;
    left: 260px;
    top: 318px;
    width: 330px;
    color: #fff;
    font-size: 20px;
    line-height: 24px;
    letter-spacing: 1px;
    white-space: nowrap;
  }
</style>
</head>
<body>

  <section class="card card--back" aria-label="Card back">
    <svg class="card__bands" viewBox="0 0 760 430" aria-hidden="true">
      <polygon points="0,372 190,372 225,312 640,312 640,352 250,352 215,410 0,410" fill="var(--navy)"/>
      <rect x="640" y="258" width="120" height="40" fill="var(--orange)"/>
      <circle cx="640" cy="310" r="42" fill="#fff" stroke="var(--navy)" stroke-width="6"/>
    </svg>
    <div class="brand">
      <div class="brand__mark"></div>
      <div class="brand__name">Tide<br>Harbor<br>Finance</div>
    </div>
    <div class="divider"></div>
    <div class="details">
      <h2 class="details__title">Our Services</h2>
      <ul class="services">
        <li><span class="tick">✓</span>Home Loans</li>
        <li><span class="tick">✓</span>Investment Loans</li><br>
        <li><span class="tick">✓</span>First Home Buyers</li>
        <li><span class="tick">✓</span>Refinancing</li><br>
        <li><span class="tick">✓</span>Car Finance</li>
      </ul>
    </div>
    <p class="slogan">Clear Options, Calm Decisions</p>
  </section>

  <section class="card card--front" aria-label="Card front">
    <svg class="card__bands" viewBox="0 0 760 430" aria-hidden="true">
      <polygon points="0,372 190,372 225,312 640,312 640,352 250,352 215,410 0,410" fill="var(--navy)"/>
      <rect x="640" y="258" width="120" height="40" fill="var(--orange)"/>
      <circle cx="640" cy="310" r="42" fill="#fff" stroke="var(--navy)" stroke-width="6"/>
    </svg>
    <div class="brand">
      <div class="brand__mark"></div>
      <div class="brand__name">Tide<br>Harbor<br>Finance</div>
    </div>
    <div class="divider"></div>
    <div class="details">
      <h2 class="person__name">Peter Colburn</h2>
      <p class="person__role">Director</p>
      <ul class="contact">
        <li>
          <svg viewBox="0 0 18 18"><rect x="5" y="1.5" width="8" height="15" rx="1.5" fill="none" stroke="var(--ink)" stroke-width="1.5"/></svg>
          0427 903186
        </li>
        <li>
          <svg viewBox="0 0 18 18"><rect x="1.5" y="4" width="15" height="10" fill="var(--navy)"/><path d="M1.5 4 L9 10 L16.5 4" fill="none" stroke="#fff" stroke-width="1.3"/></svg>
          peter@tideharborfinance.com.au
        </li>
        <li>
          <svg viewBox="0 0 18 18"><g fill="none" stroke="var(--navy)" stroke-width="1.3"><circle cx="9" cy="9" r="7.5"/><ellipse cx="9" cy="9" rx="3.2" ry="7.5"/><path d="M1.5 9h15M3 5h12M3 13h12"/></g></svg>
          www.tideharborfinance.com.au
        </li>
      </ul>
    </div>
    <p class="slogan">Clear Options, Calm Decisions</p>
  </section>

</body>
</html>
```